2 Business Card Designs

Need two business cards designed:
1) for lumora studio (wedding video) website is lumorastudio.com.au
2) for lumora studio (corporate video) website is lumorastudio.net.au

I am looking for something simple, no fancy shapes etc. Just elegant, simple and classy.

Both companies are video companies, one specialising in weddings the other corporate videos. Neither card needs to have any pics of video or camera related images. Please use same colour schemes as respective websites.

Logo is the same but can change colour.

Industry/Entity Type

Camera

Requirements
Must have
• Logo should be either all white or a colour to match websites
Should not have
• swirls, flowers, shapes, etc.

```html
<!DOCTYPE html>
<html lang="en">
<head>
<meta charset="utf-8">
<title>Lumora Studio – Business Cards</title>
<link rel="stylesheet" href="https://fonts.googleapis.com/css2?family=Roboto:wght@300&display=swap">
<style>
  :root {
    --page: #ffffff;
    --sage-light: #e1e3d3;
    --sage-mid: #cfd1bc;
    --sage-edge: #b9bba3;
    --sage-ink: #6a6b5c;
    --sage-band: #6a6a5a;
    --sage-band-top: #8b8b78;
    --sage-band-ink: #e2e3d3;
    --sage-rule: #c9cab5;
    --slate-deep: #2a3036;
    --slate-mid: #30373e;
    --slate-ink: #53687a;
    --slate-band: #465762;
    --slate-band-ink: #2e3942;
    --steel-light: #4a5962;
    --steel-edge: #36424b;
    --steel-ink: #aeb8be;
    --shadow: rgba(0, 0, 0, 0.55);
    --text-font: "Roboto", sans-serif;
  }
  * { box-sizing: border-box; margin: 0; padding: 0; }
  html, body {
    width: 1200px; height: 1200px; overflow: hidden;
    background: var(--page);
  }
  .sheet { position: relative; width: 1200px; height: 1200px; font-family: var(--text-font); font-weight: 300; }

  .card {
    position: absolute;
    width: 594px; height: 363px;
    border-radius: 12px;
    overflow: hidden;
    box-shadow: 2px 4px 7px var(--shadow);
  }
  .card--front { z-index: 2; }
  .card--back { z-index: 1; }

  .card--wedding-front { left: 18px; top: 22px; }
  .card--wedding-back { left: 588px; top: 270px; }
  .card--corporate-front { left: 18px; top: 571px; }
  .card--corporate-back { left: 588px; top: 821px; }

  .theme-sage {
    background: radial-gradient(ellipse 60% 65% at 50% 45%, var(--sage-light), var(--sage-mid) 55%, var(--sage-edge));
    color: var(--sage-ink);
  }
  .theme-slate {
    background: linear-gradient(180deg, var(--slate-mid), var(--slate-deep));
    color: var(--slate-ink);
  }
  .theme-steel {
    background: radial-gradient(ellipse 70% 70% at 40% 25%, var(--steel-light), var(--steel-edge));
    color: var(--steel-ink);
  }

  /* front: company name */
  .front-name {
    position: absolute; left: 0; top: 110px; width: 100%;
    text-align: center;
    font-size: 76px; line-height: 1;
    white-space: nowrap;
  }
  .front-url {
    position: absolute; left: 0; width: 100%; top: 250px;
    text-align: center;
    font-size: 21px;
  }

  .front-band {
    position: absolute; left: 0; bottom: 0;
    width: 100%; height: 58px;
  }
  .theme-sage .front-band {
    background: var(--sage-band);
    border-top: 8px solid var(--sage-band-top);
    color: var(--sage-band-ink);
  }
  .theme-slate .front-band {
    background: var(--slate-band);
    color: var(--slate-band-ink);
  }
  .front-band__text {
    position: absolute; left: 0; width: 100%; top: 7px;
    text-align: center;
    font-size: 27px;
    white-space: nowrap;
  }
  .theme-slate .front-band__text { top: 12px; font-size: 26px; }
  .front-band__rules { position: absolute; left: 0; top: 14px; }

  /* back */
  .back-title {
    position: absolute; left: 29px; top: 34px;
    font-size: 34px; font-weight: 300; line-height: 1;
  }
  .back-role {
    position: absolute; left: 29px; top: 78px;
    font-size: 27px; line-height: 1;
  }
  .back-name {
    position: absolute; right: 22px; top: 50px;
    font-size: 36px; line-height: 1;
    white-space: nowrap;
  }
  .back-rule { position: absolute; left: 318px; top: 98px; }
  .back-address {
    position: absolute; right: 22px; top: 122px;
    text-align: right;
    font-size: 25px; line-height: 31px;
  }
  .back-contact {
    position: absolute; left: 29px; top: 238px;
    font-size: 27px; line-height: 35px;
    border-collapse: collapse;
  }
  .back-contact td { padding: 0; white-space: nowrap; }
  .back-contact__label { text-align: right; width: 92px; padding-right: 6px !important; }
</style>
</head>
<body>
<main class="sheet">

  <!-- Wedding video: front -->
  <section class="card card--front card--wedding-front theme-sage">
    <p class="front-name">lumora studio</p>
    <p class="front-url">www.LumoraStudio.com.au</p>
    <div class="front-band">
      <svg class="front-band__rules" width="594" height="20" viewBox="0 0 594 20" aria-hidden="true">
        <g stroke="var(--sage-rule)" stroke-width="1.5" fill="var(--sage-rule)">
          <line x1="0" y1="10" x2="104" y2="10"/>
          <circle cx="104" cy="10" r="2.5"/>
          <line x1="494" y1="10" x2="594" y2="10"/>
          <circle cx="494" cy="10" r="2.5"/>
        </g>
      </svg>
      <p class="front-band__text">Sydney Wedding Video</p>
    </div>
  </section>

  <!-- Wedding video: back -->
  <section class="card card--back card--wedding-back theme-sage">
    <h2 class="back-title">Project Owner</h2>
    <p class="back-role">Director</p>
    <p class="back-name">lumora studio</p>
    <svg class="back-rule" width="276" height="10" viewBox="0 0 276 10" aria-hidden="true">
      <line x1="4" y1="5" x2="276" y2="5" stroke="var(--sage-ink)" stroke-width="2"/>
      <circle cx="4" cy="5" r="3" fill="var(--sage-ink)"/>
    </svg>
    <p class="back-address">218 Harbour Parade<br>Lindfield :: NSW :: 2070</p>
    <table class="back-contact">
      <tr><td class="back-contact__label">tel ::</td><td>+61 2 9000 4821</td></tr>
      <tr><td class="back-contact__label">email ::</td><td>lumorastudio@example.com.au</td></tr>
      <tr><td class="back-contact__label">web ::</td><td>www.lumorastudio.com.au</td></tr>
    </table>
  </section>

  <!-- Corporate video: front -->
  <section class="card card--front card--corporate-front theme-slate">
    <p class="front-name">lumora studio</p>
    <p class="front-url">www.LumoraStudio.net.au</p>
    <div class="front-band">
      <p class="front-band__text">Creating Corporate Videos for Your Company</p>
    </div>
  </section>

  <!-- Corporate video: back -->
  <section class="card card--back card--corporate-back theme-steel">
    <h2 class="back-title">Project Owner</h2>
    <p class="back-role">Director</p>
    <p class="back-name">lumora studio</p>
    <svg class="back-rule" width="276" height="10" viewBox="0 0 276 10" aria-hidden="true">
      <line x1="4" y1="5" x2="276" y2="5" stroke="var(--steel-ink)" stroke-width="2"/>
      <circle cx="4" cy="5" r="3" fill="var(--steel-ink)"/>
    </svg>
    <p class="back-address">218 Harbour Parade<br>Lindfield :: NSW :: 2070</p>
    <table class="back-contact">
      <tr><td class="back-contact__label">tel ::</td><td>+61 2 9000 1357</td></tr>
      <tr><td class="back-contact__label">email ::</td><td>lumorastudio@example.net.au</td></tr>
      <tr><td class="back-contact__label">web ::</td><td>www.lumorastudio.net.au</td></tr>
    </table>
  </section>

</main>
</body>
</html>
```